Website Refresh for Niche Pet Website

We have a site that needs a fresh, modern look. This site gets approx 500K views a month and we want a re-design.

Category layout
New blog template layout

We need to keep the large rolling ads on the home page
The small ad need to be placed on the side when looking at the interior page.

We need a modern slick easy to use site

Target Market(s)

Breeders and pet buyers in the UK

Industry/Entity Type

pets

Number of Pages Required

4 page

Requirements
Must have
• Be Gun Dog specific - these are for working homes. Creative way to showcase the ads, breeds etc.
Nice to have
• We are open to logo improvements and colour, however, this is the UK market for buying and selling gun dogs. The grren and gold do work well.

```html
<!DOCTYPE html>
<html lang="en">
<head>
<meta charset="utf-8">
<title>Covert Hounds – Find Your Perfect Gundog</title>
<link rel="stylesheet" href="https://fonts.googleapis.com/css2?family=Unbounded:wght@700;800&family=Roboto:wght@400;500;700&display=swap">
<style>
:root{
  --bg:#000;
  --ink:#fff;
  --gold:#c9a437;
  --gold-dark:#a8862a;
  --olive:#1c1d10;
  --olive-line:#3a3a22;
  --contact:#3f3311;
  --field:#5a4a1b;
  --footer:#141410;
  --muted:#cfcfcf;
}
*{box-sizing:border-box;margin:0;padding:0}
html,body{width:1200px;height:4281px;overflow:hidden}
body{background:var(--bg);color:var(--ink);font-family:'Roboto',sans-serif;position:relative}
.abs{position:absolute}
.display{font-family:'Unbounded',sans-serif;font-weight:800;text-transform:uppercase;letter-spacing:.5px;white-space:nowrap}

/* header */
.brand{left:60px;top:42px;display:flex;align-items:center;gap:12px}
.brand-dot{width:46px;height:46px;border-radius:50%;background:var(--gold)}
.brand-name{font-family:'Roboto',sans-serif;font-weight:700;font-size:34px;color:var(--gold);line-height:1}
.brand-est{left:118px;top:92px;font-size:11px;color:var(--ink)}
.main-nav{left:507px;top:57px;display:flex;font-size:13px}
.main-nav a{color:var(--ink);text-decoration:none;margin-right:58px}
.nav-rule{left:507px;top:91px;width:631px;height:1px;background:#7a7a7a}
.menu-icon{left:1116px;top:56px}

/* hero */
.hero-media{left:548px;top:108px;width:585px;height:440px;background:radial-gradient(ellipse at 65% 40%,#1f1f22 0%,#0c0c0d 55%,#050505 100%)}
.hero-title{left:60px;top:222px;font-size:43px;line-height:76px;letter-spacing:0;z-index:2}
.hero-rule{left:60px;top:371px;width:518px;border-top:1px dotted #8a8a8a;z-index:2}
.hero-gold{left:60px;top:392px;font-size:43px;letter-spacing:0;color:var(--gold);z-index:2}
.play{left:819px;top:282px}

/* search */
.search{left:306px;top:603px;width:586px;height:78px;background:var(--olive);border-radius:4px}
.search-label{left:22px;top:26px;font-size:20px;color:var(--gold);font-weight:500}
.select{left:197px;top:24px;width:293px;height:33px;border:1px solid var(--gold);border-radius:17px;font-size:10px;padding:10px 14px;color:var(--ink)}
.select svg{position:absolute;right:12px;top:10px}
.search-btn{left:500px;top:24px;width:63px;height:33px;background:var(--gold);border-radius:17px}
.search-btn svg{position:absolute;left:22px;top:7px}

/* categories */
.cat-media{left:432px;top:706px;width:349px;height:175px;background:radial-gradient(ellipse at 50% 40%,#1b1c22,#060606 75%)}
.section-head{display:flex;align-items:center;gap:22px;color:var(--gold);font-size:31px}
.section-head .line{flex:1;height:1px;background:var(--gold-dark)}
.cat-head{left:91px;top:782px;width:1016px}
.cat-card{top:849px;width:138px;height:126px;background:#fff;border-radius:3px;color:#111;font-size:12px;font-weight:500;text-align:center}
.cat-card.active{background:var(--gold);color:#fff}
.cat-card .thumb{width:66px;height:66px;border-radius:50%;margin:15px auto 14px}

/* featured slider */
.slider{left:141px;top:1045px;width:916px;height:424px;background:var(--olive);border:4px solid var(--olive-line)}
.slider-media{left:432px;top:0;width:476px;height:416px;background:linear-gradient(160deg,#121212,#050505)}
.slider-title{left:0;top:16px;width:916px;text-align:center;font-size:48px;color:var(--gold);font-weight:800;font-family:'Unbounded',sans-serif;white-space:nowrap}
.slider-photo{left:114px;top:87px}
.perk-list{left:430px;top:133px;list-style:none;font-size:25px}
.perk-list li{display:flex;align-items:center;gap:22px;height:58px}
.slider-link{left:487px;top:352px;color:var(--gold);font-size:21px}
.arrow{top:1236px}

/* listings */
.listing{top:1527px;width:356px;height:351px}
.listing .photo{height:270px}
.listing .band{height:81px;background:var(--gold);padding:14px 18px 0;position:relative}
.listing .meta{display:flex;justify-content:space-between;font-size:12px}
.listing .price{font-size:20px;margin-top:14px}
.listing .go{position:absolute;right:18px;top:42px;width:66px;height:27px;border-radius:14px;background:#000}
.listing .go svg{position:absolute;left:15px;top:9px}

/* welcome */
.welcome-head{left:91px;top:1950px;width:1016px;font-size:29px}
.copy{font-size:12.5px;line-height:22.4px;color:var(--ink)}
.welcome-copy{left:146px;top:2018px;width:908px;text-align:center}
.welcome-copy p+p{margin-top:22px}

/* feature blocks */
.feature-head{font-size:29px;color:var(--gold);line-height:45px}
.deposit-head{left:545px;top:2238px}
.deposit-copy{left:630px;top:2364px;width:472px}
.buy-head{left:115px;top:2752px}
.buy-copy{left:184px;top:2824px;width:472px}
.copy a{color:var(--gold);text-decoration:none}

/* contact */
.contact{left:57px;top:3299px;width:1080px;height:436px;background:var(--contact)}
.contact-head{left:61px;top:40px;font-size:29px}
.contact-rule{left:61px;top:96px;width:424px;height:1px;background:#6c5a25}
.field{left:63px;width:423px;height:28px;background:var(--field);font-size:12px;padding:7px 20px}
.send{left:63px;top:356px;width:104px;height:30px;border-radius:15px;background:var(--gold);font-size:11px;text-align:center;line-height:30px}
.contact-brand{left:594px;top:147px;width:354px;display:flex;justify-content:center;align-items:center;gap:12px}
.contact-brand .brand-name{color:var(--ink);font-size:36px}
.contact-brand .brand-dot{background:var(--ink);width:50px;height:50px}
.contact-rule2{left:594px;top:248px;width:354px;height:1px;background:#6c5a25}
.mail-icon{left:762px;top:279px}
.contact-email{left:594px;top:310px;width:354px;text-align:center;font-size:14px}
.socials{display:flex;gap:10px}
.socials span{width:20px;height:20px;border-radius:50%;background:var(--ink);display:block}
.contact-social{left:744px;top:352px}

/* partners */
.partner-frame{left:68px;top:3806px;width:253px;height:219px;border:1px solid #bbb}
.partner{top:3820px;width:236px;height:199px}

/* footer */
.footer{left:0;top:4105px;width:1200px;height:176px;background:var(--footer)}
.footer a{color:#fff;text-decoration:none}
.quick{left:60px;top:30px;font-size:21px;color:var(--gold)}
.foot-links{top:75px;font-size:12.5px}
.foot-links2{top:119px;font-size:12.5px}
.copyright{right:62px;top:119px;font-size:12.5px}
.foot-social{right:62px;top:73px}
.foot-social span{width:20px;height:20px;background:#fff}
</style>
</head>
<body>

<header>
  <div class="abs brand"><span class="brand-dot"></span><span class="brand-name">Covert Hounds</span></div>
  <div class="abs brand-est">— Est 2002 —</div>
  <nav class="abs main-nav"><a href="#">Lost/Stolen Dogs</a><a href="#">Events</a><a href="#">Information</a></nav>
  <div class="abs nav-rule"></div>
  <svg class="abs menu-icon" width="22" height="18" viewBox="0 0 22 18"><path d="M8 2h14M2 9h20M10 16h12" stroke="#c9a437" stroke-width="2"/></svg>
</header>

<section class="hero">
  <div class="abs hero-media" role="img" aria-label="Black labrador portrait against a dark background"></div>
  <h1 class="abs display hero-title">Find your<br>perfect</h1>
  <div class="abs hero-rule"></div>
  <div class="abs display hero-gold">Gundog today</div>
  <svg class="abs play" width="40" height="40" viewBox="0 0 40 40"><circle cx="20" cy="20" r="18" fill="none" stroke="#c9a437" stroke-width="2"/><path d="M16 13l10 7-10 7z" fill="#c9a437"/></svg>
</section>

<form class="abs search">
  <div class="abs search-label">Find a Gundog</div>
  <div class="abs select">Select County<svg width="14" height="10" viewBox="0 0 14 10"><path d="M1 2l6 6 6-6" stroke="#c9a437" stroke-width="1.5" fill="none"/></svg></div>
  <div class="abs search-btn"><svg width="20" height="20" viewBox="0 0 20 20"><circle cx="9" cy="9" r="6.5" stroke="#000" stroke-width="2" fill="none"/><path d="M14 14l4 4" stroke="#000" stroke-width="2"/></svg></div>
</form>

<section class="categories">
  <div class="abs cat-media" role="img" aria-label="Black labrador in shadow"></div>
  <h2 class="abs display section-head cat-head"><span class="line"></span>Categories<span class="line"></span></h2>
  <div class="abs cat-card active" style="left:111px"><div class="thumb" role="img" aria-label="Labrador photo" style="background:#6b7050"></div>Labradors</div>
  <div class="abs cat-card" style="left:279px"><div class="thumb" role="img" aria-label="Springer spaniel photo" style="background:#8a8f7c"></div>Springer Spaniels</div>
  <div class="abs cat-card" style="left:447px"><div class="thumb" role="img" aria-label="Cocker spaniel photo" style="background:#6d7a4c"></div>Cocker Spaniels</div>
  <div class="abs cat-card" style="left:615px"><div class="thumb" role="img" aria-label="Stolen dog photo" style="background:#b07a48"></div>Stolen Dogs</div>
  <div class="abs cat-card" style="left:783px"><div class="thumb" role="img" aria-label="Field trial photo" style="background:#7c7d5a"></div>Events &amp; Trials</div>
  <div class="abs cat-card" style="left:951px"><div class="thumb" role="img" aria-label="Group of gundogs photo" style="background:#5d4630"></div>Place An Advert</div>
</section>

<section class="abs slider">
  <div class="abs slider-media" role="img" aria-label="Dark labrador photograph"></div>
  <div class="abs slider-title">Harrowmere Labradors</div>
  <svg class="abs slider-photo" width="280" height="280" viewBox="0 0 280 280" role="img" aria-label="Two chocolate labrador puppies"><circle cx="140" cy="140" r="139" fill="#dedede"/><ellipse cx="140" cy="115" rx="95" ry="75" fill="#4a2a1c"/></svg>
  <ul class="abs perk-list">
    <li><svg width="18" height="18" viewBox="0 0 18 18"><path d="M2 3h14l-7 13z" fill="#c9a437"/></svg>Qualified &amp; Licensed Breeder</li>
    <li><svg width="18" height="18" viewBox="0 0 18 18"><path d="M2 3h14l-7 13z" fill="#c9a437"/></svg>Stud Dogs</li>
    <li><svg width="18" height="18" viewBox="0 0 18 18"><path d="M2 3h14l-7 13z" fill="#c9a437"/></svg>Part Trained Dogs</li>
  </ul>
  <div class="abs slider-link">Harrowmerelabradors.Co.Uk</div>
</section>
<svg class="abs arrow" style="left:62px" width="26" height="44" viewBox="0 0 26 44"><path d="M23 2L3 22l20 20" stroke="#c9a437" stroke-width="3" fill="none"/></svg>
<svg class="abs arrow" style="left:1110px" width="26" height="44" viewBox="0 0 26 44"><path d="M3 2l20 20L3 42" stroke="#c9a437" stroke-width="3" fill="none"/></svg>

<section class="listings">
  <article class="abs listing" style="left:60px">
    <div class="photo" role="img" aria-label="Liver spaniel sitting in autumn leaves" style="background:linear-gradient(160deg,#3a281c,#5a4030 60%,#2a1d15)"></div>
    <div class="band"><div class="meta"><span>Lichfield , Staffordshire</span><span>10th October 2023</span></div><div class="price">£1000.00</div>
    <span class="go"><svg width="36" height="10" viewBox="0 0 36 10"><path d="M0 5h34M29 1l5 4-5 4" stroke="#fff" stroke-width="1.5" fill="none"/></svg></span></div>
  </article>
  <article class="abs listing" style="left:422px">
    <div class="photo" role="img" aria-label="Black labrador on a grass lawn" style="background:linear-gradient(180deg,#6e8a3e,#58752f)"></div>
    <div class="band"><div class="meta"><span>Downham Market, Norfolk</span><span>10th October 2023</span></div><div class="price">£3000.00</div>
    <span class="go"><svg width="36" height="10" viewBox="0 0 36 10"><path d="M0 5h34M29 1l5 4-5 4" stroke="#fff" stroke-width="1.5" fill="none"/></svg></span></div>
  </article>
  <article class="abs listing" style="left:783px">
    <div class="photo" role="img" aria-label="Springer spaniel among heather" style="background:linear-gradient(160deg,#5b6b45,#8a7c8c 55%,#6a6a50)"></div>
    <div class="band"><div class="meta"><span>Southampton , Hampshire</span><span>10th October 2023</span></div><div class="price">£1700.00</div>
    <span class="go"><svg width="36" height="10" viewBox="0 0 36 10"><path d="M0 5h34M29 1l5 4-5 4" stroke="#fff" stroke-width="1.5" fill="none"/></svg></span></div>
  </article>
</section>

<section class="welcome">
  <h2 class="abs display section-head welcome-head"><span class="line"></span>Welcome to Covert Hounds<span class="line"></span></h2>
  <div class="abs copy welcome-copy">
    <p>Our aim at CovertHounds has always been to provide the very best gundog advertisement platform to purchase and sell your gundogs in the safest possible way. CovertHounds was created by gundog people that know your time is valuable and best spent in the field with your dogs, thats why we have no lengthy registration forms to fill in or no accounts to remember passwords for adverts you posted 3 months ago.</p>
    <p>Here at CovertHounds your advert stays on until sold and all we ask in return is that you keep your advert updated with our email edit links so our customers looking to purchase their new gun dog can make the best informed decisions.</p>
  </div>
</section>

<section class="deposit">
  <svg class="abs" style="left:0;top:2200px" width="640" height="540" viewBox="0 2200 640 540" role="img" aria-label="Shooter in reeds with a black labrador leaping"><defs><linearGradient id="gDep" x1="0" y1="0" x2="1" y2="1"><stop offset="0" stop-color="#c8cbd0"/><stop offset=".5" stop-color="#7d7560"/><stop offset="1" stop-color="#5c4a30"/></linearGradient></defs><path d="M150 2252L566 2400L240 2684Z" fill="url(#gDep)" stroke="url(#gDep)" stroke-width="30" stroke-linejoin="round"/></svg>
  <h2 class="abs display feature-head deposit-head">CovertHounds safe<br>deposit service</h2>
  <p class="abs copy deposit-copy">Your safety is our number one priority when purchasing a gun dog and we have teamed up with SafeHold who have tailor made a gundog escrow just for YOU, so now you can pay deposits for gun dogs safely without the fear of being scammed and losing deposits for your new gun dog. We have made the CovertHounds Safe Deposit Service FREE for all breeders to use so there is really no good reason not to support the service and help keep the buyers safe when they part with large sums of money.<br>To know more about the CovertHounds Safe Deposit Service and how it works please watch this video <a href="#">https://www.clipreel.tv/watch?v=sd24FhQ</a></p>
</section>

<section class="connect">
  <h2 class="abs display feature-head buy-head">Buy, sell &amp; connect</h2>
  <p class="abs copy buy-copy">When you post an advert with CovertHounds you will be sent a email confirmation (check spam folder) on that email you will find an edit link that allows you to edit your gundog advert when you like, we advice you keep the email safe for future use. If you post an advert we ask that you keep them up to date at all times. When you sell your gundog you can edit your own advert and mark the dog has sold. If the advert is left for over 3 months without any edits we will automatically delete the advert, this is to stop old adverts blocking up the site.<br>We are here to serve the gun dog community and to do that we have set up Stolen Dogs and Events &amp; Trails category's which is FREE to advertise. We want our customers to work with us to eliminate stolen working dogs and connect through gun dog events up and down the UK. CovertHounds is passionate about all things gundogs and we know you are too. Should you need any further assistance please email <a href="#">hello@coverthounds.co.uk</a></p>
  <svg class="abs" style="left:680px;top:2730px" width="480" height="500" viewBox="680 2730 480 500" role="img" aria-label="Dog retrieving a duck through water"><defs><linearGradient id="gBuy" x1="0" y1="0" x2="1" y2="1"><stop offset="0" stop-color="#1c2a2e"/><stop offset=".5" stop-color="#5f6b6e"/><stop offset="1" stop-color="#1a2428"/></linearGradient></defs><path d="M738 2768L1118 2910L806 3194Z" fill="url(#gBuy)" stroke="url(#gBuy)" stroke-width="30" stroke-linejoin="round"/></svg>
</section>

<section class="abs contact">
  <h2 class="abs display contact-head">Contact us</h2>
  <div class="abs contact-rule"></div>
  <div class="abs field" style="top:130px">Your Name</div>
  <div class="abs field" style="top:168px">Your Email</div>
  <div class="abs field" style="top:208px">Your Phone Number</div>
  <div class="abs field" style="top:246px;height:97px">Your Message</div>
  <div class="abs send">SEND</div>
  <div class="abs contact-brand"><span class="brand-dot"></span><span class="brand-name">Covert Hounds</span></div>
  <div class="abs contact-rule2"></div>
  <svg class="abs mail-icon" width="20" height="14" viewBox="0 0 20 14"><rect width="20" height="14" rx="1" fill="#fff"/><path d="M1 1l9 7 9-7" stroke="#3f3311" stroke-width="1.5" fill="none"/></svg>
  <div class="abs contact-email">hello@coverthounds.co.uk</div>
  <div class="abs socials contact-social"><span></span><span></span></div>
</section>

<section class="partners">
  <div class="abs partner-frame"></div>
  <div class="abs partner" style="left:91px;top:3820px;width:208px;height:183px;background:linear-gradient(160deg,#b9a46a,#6d4a2c)" role="img" aria-label="Advert for downlandgundogsupplies.co.uk with a spaniel"></div>
  <div class="abs partner" style="left:347px;background:linear-gradient(90deg,#7a5a3a,#c9a55a)" role="img" aria-label="Advert for Harrowmere Labradors with a chocolate labrador"></div>
  <div class="abs partner" style="left:605px;background:#fff" role="img" aria-label="Advert for Paws@Elmfield gun dog supplies"></div>
  <div class="abs partner" style="left:863px;background:linear-gradient(135deg,#5a2f6e,#8a7a3a 60%,#6a5a30)" role="img" aria-label="Advert for Thornley's Fieldmaster dog food with a spaniel"></div>
</section>

<footer class="abs footer">
  <div class="abs quick">Quick Links</div>
  <a class="abs foot-links" style="left:60px" href="#">Home</a>
  <a class="abs foot-links" style="left:163px" href="#">Information</a>
  <a class="abs foot-links" style="left:299px" href="#">Buyer Deposit Service</a>
  <a class="abs foot-links" style="left:499px" href="#">Contact Us</a>
  <div class="abs socials foot-social"><span></span><span></span></div>
  <a class="abs foot-links2" style="left:60px" href="#">Terms &amp; Conditions</a>
  <a class="abs foot-links2" style="left:249px" href="#">Privacy Policy</a>
  <div class="abs copyright">© Copyright Covert Hounds 2023.</div>
</footer>

</body>
</html>
```